Save our Business Card - We need your help

We need a fresh look on our business cards. We like it as it is, but it's not quite getting the 'wow' effect that we desire.
We're a tech startup building a cloud based solution for retailers consisting of Point of Sale, Inventory management and CRM.
The design should communicate a sense of a company that cares about the little things, design and relationships.
You can have a look at our website www.tillnest.com to get a feel for what we're like. Please feel free to message us for any further clarification
Target Market(s)
Our Customers are retail busines owners, cafe owners, other startups etc.
Industry/Entity Type
Building
Colors
Designer to choose colors to be used in the design.
Look and feel
Each slider illustrates characteristics of the customer's brand and the style your logo design should communicate.

```html
<!DOCTYPE html>
<html lang="en">
<head>
<meta charset="utf-8">
<title>TillNest Business Card</title>
<link rel="stylesheet" href="https://fonts.googleapis.com/css2?family=Lato:wght@400;700;900&display=swap">
<style>
  :root {
    --bg: #e9e6e1;
    --orange-light: #f9c326;
    --orange: #f2a51c;
    --orange-deep: #e8891a;
    --white: #ffffff;
    --off-white: #f3f3f3;
    --charcoal: #3a3a3c;
    --charcoal-light: #5a5a5c;
    --text-light: #ffffff;
    --shadow: rgba(0,0,0,0.22);
  }
  * { box-sizing: border-box; margin: 0; padding: 0; }
  html, body {
    width: 1200px; height: 1023px; overflow: hidden;
    background: var(--bg);
    font-family: "Lato", Arial, sans-serif;
  }
  .canvas { position: relative; width: 1200px; height: 1023px; }

  .card {
    position: absolute;
    width: 660px; height: 378px;
    border-radius: 4px;
    overflow: hidden;
    box-shadow: 0 14px 30px var(--shadow);
  }

  /* Front card */
  .card--front {
    left: 70px; top: 80px;
    background: radial-gradient(circle at 60% 40%, var(--orange-light), var(--orange) 55%, var(--orange-deep));
  }
  .front__side-band {
    position: absolute; left: 0; top: 0; bottom: 0; width: 150px;
    background: linear-gradient(90deg, var(--off-white), var(--white));
  }
  .front__mark {
    position: absolute; left: 52px; top: 112px;
    width: 46px; height: 46px; background: var(--orange);
  }
  .front__top-bar {
    position: absolute; left: 376px; right: 0; top: 62px; height: 30px;
    background: var(--white);
  }
  .front__brand {
    position: absolute; left: 196px; top: 58px;
    font-size: 34px; font-weight: 900; color: var(--text-light);
    letter-spacing: 0.5px;
  }
  .front__person {
    position: absolute; right: 48px; top: 158px; text-align: right;
    color: var(--text-light);
  }
  .front__name { font-size: 18px; font-weight: 700; }
  .front__role { font-size: 14px; font-weight: 400; margin-top: 2px; }
  .front__contacts {
    position: absolute; left: 196px; top: 232px;
    list-style: none; color: var(--text-light); font-size: 14px;
  }
  .front__contacts li { display: flex; align-items: center; gap: 10px; height: 27px; }
  .contact-icon { width: 16px; height: 16px; flex: none; }

  /* Back card */
  .card--back {
    left: 470px; top: 540px;
    background: var(--white);
  }
  .back__band {
    position: absolute; left: 0; right: 0; bottom: 0; height: 172px;
    background: linear-gradient(100deg, var(--charcoal), var(--charcoal-light) 45%, var(--charcoal));
  }
  .back__url {
    position: absolute; left: 60px; bottom: 72px;
    font-size: 24px; font-weight: 400; color: var(--text-light); letter-spacing: 0.5px;
  }
  .back__logo {
    position: absolute; left: 0; right: 0; top: 58px;
    display: flex; align-items: center; justify-content: center; gap: 22px;
  }
  .back__mark { width: 72px; height: 72px; background: var(--orange); }
  .back__brand { font-size: 64px; font-weight: 900; color: var(--orange); }
</style>
</head>
<body>
<main class="canvas">
  <section class="card card--front" aria-label="Card front">
    <div class="front__side-band"></div>
    <div class="front__mark"></div>
    <div class="front__top-bar"></div>
    <div class="front__brand">TillNest</div>
    <div class="front__person">
      <div class="front__name">Dana Hollis</div>
      <div class="front__role">Chief Executive</div>
    </div>
    <ul class="front__contacts">
      <li>
        <svg class="contact-icon" viewBox="0 0 16 16"><rect x="4" y="1" width="8" height="14" rx="1.5" fill="none" stroke="#fff" stroke-width="1.5"/><circle cx="8" cy="12.5" r="0.9" fill="#fff"/></svg>
        00 987 654 321
      </li>
      <li>
        <svg class="contact-icon" viewBox="0 0 16 16"><circle cx="8" cy="8" r="6.5" fill="none" stroke="#fff" stroke-width="1.4"/><path d="M1.5 8h13M8 1.5c-3 3.5-3 9.5 0 13M8 1.5c3 3.5 3 9.5 0 13" fill="none" stroke="#fff" stroke-width="1"/></svg>
        www.tillnest.com
      </li>
      <li>
        <svg class="contact-icon" viewBox="0 0 16 16"><rect x="1.5" y="3.5" width="13" height="9" fill="none" stroke="#fff" stroke-width="1.4"/><path d="M1.5 3.5 8 9l6.5-5.5" fill="none" stroke="#fff" stroke-width="1.4"/></svg>
        hello@tillnest.com
      </li>
    </ul>
  </section>

  <section class="card card--back" aria-label="Card back">
    <div class="back__logo">
      <div class="back__mark"></div>
      <div class="back__brand">TillNest</div>
    </div>
    <div class="back__band"></div>
    <div class="back__url">www.tillnest.com</div>
  </section>
</main>
</body>
</html>
```